Garden Maintenance business card

I need a business card design for my new business "Silver Birch Garden Co". I do garden maintenance including lawns, turf lawn, pruning, hedging, water systems, anything related to the garden really (dont think i need to include any of that except garden maintenance)

Reason: narrowed it down and just showing my business partners the designs, cheers

Industry/Entity Type

Business

Requirements
Must have
• Must Have:
- ABN: XX XXX XXX XXX
Mobile phone number 00 0000000
email address xxxx.xxxxxx@gmail.com
Owner Name Xxxx xxxxxx
title: garden specialist possibly under name or something sounding professional
logo which has been submitted both with a background and one without, feel free to choose whichever one you like
business name

```html
<!DOCTYPE html>
<html lang="en">
<head>
<meta charset="utf-8">
<title>Silver Birch Garden Co — Business Card</title>
<link href="https://fonts.googleapis.com/css2?family=PT+Sans:wght@400&display=swap" rel="stylesheet">
<style>
  :root {
    --card-green: #9fc59b;
    --card-green-light: #b3d2ae;
    --card-green-soft: #aacca6;
    --ink-dark: #1d1f1c;
    --ink-light: #f5f8f1;
    --page: #ffffff;
  }
  html, body {
    margin: 0;
    padding: 0;
    width: 857px;
    height: 1200px;
    overflow: hidden;
    background: var(--page);
  }
  .canvas {
    position: relative;
    width: 857px;
    height: 1200px;
    font-family: "PT Sans", "Myriad Pro", Arial, sans-serif;
  }
  .card {
    position: absolute;
    left: 0;
    width: 857px;
    height: 514px;
    background: var(--card-green);
    overflow: hidden;
  }
  .card--front { top: 0; }
  .card--back { top: 686px; }

  .brand-mark {
    position: absolute;
    left: 90px;
    top: 120px;
    width: 250px;
    height: 250px;
    border-radius: 50%;
    background: var(--card-green-light);
  }
  .brand-name {
    position: absolute;
    left: 400px;
    top: 110px;
    margin: 0;
    font-weight: 400;
    font-size: 60px;
    line-height: 66px;
    color: var(--ink-dark);
  }
  .brand-name span { display: block; }
  .brand-name .line-1 { padding-left: 30px; }
  .brand-name .line-2 { padding-left: 110px; }
  .brand-name .line-3 { padding-left: 110px; }
  .brand-name .line-4 { padding-left: 150px; }

  .flourish {
    position: absolute;
    left: 230px;
    top: 60px;
    width: 400px;
    height: 400px;
    border-radius: 40%;
    background: radial-gradient(ellipse at center, var(--card-green-soft) 0%, var(--card-green) 70%);
  }
  .contact {
    position: absolute;
    left: 0;
    right: 0;
    top: 152px;
    margin: 0;
    text-align: center;
    font-style: normal;
    font-size: 30px;
    line-height: 38px;
    color: var(--ink-light);
  }
  .contact span { display: block; }
</style>
</head>
<body>
<div class="canvas">
  <section class="card card--front">
    <div class="brand-mark" aria-hidden="true"></div>
    <h1 class="brand-name">
      <span class="line-1">Silver</span>
      <span class="line-2">Birch</span>
      <span class="line-3">Garden</span>
      <span class="line-4">Co</span>
    </h1>
  </section>

  <section class="card card--back">
    <div class="flourish" role="img" aria-label="Faint decorative swirl flourish behind the contact details"></div>
    <address class="contact">
      <span>ABN: XX XXX XXX XXX</span>
      <span>Mobile: 00 0000000</span>
      <span>Email: xxxx.xxxxxx@gmail.com</span>
      <span>Owner Name Xxxx Xxxxxx</span>
      <span>Garden Specialist</span>
    </address>
  </section>
</div>
</body>
</html>
```